Tavi Academy

I need different posters for a high school that displays positive messaging and the school's core values.
Want the design to look sleek for high school aged children

1. Poster #1
CORE VALUES:
• RESPECT
• RESPONSIBILITY
• LEADERSHIP
• PRIDE
• COMMUNITY

2. Acronym posters for the school
Empathy
Zeal
Respect
Aspire

3. additional acronym poster
Encourage
Zenith
Relationships
Accountability

```html
<!DOCTYPE html>
<html lang="en">
<head>
<meta charset="utf-8">
<title>Tavi Academy – Core Values Poster</title>
<link rel="stylesheet" href="https://fonts.googleapis.com/css2?family=Archivo:wdth,wght@125,700&family=Nunito:wght@800&display=swap">
<style>
  :root {
    --backdrop: #d9d9d9;
    --navy: #283878;
    --mid-blue: #1f68a8;
    --sky: #22a8dc;
    --white: #ffffff;
    --respect: #6cc6a0;
    --responsibility: #8a52a3;
    --leadership: #f7ae6a;
    --pride: #c8b292;
    --community: #e966a6;
    --gold: #e3ad2b;
  }
  * { box-sizing: border-box; margin: 0; padding: 0; }
  html, body {
    width: 1200px; height: 1200px; overflow: hidden;
    background: var(--backdrop);
  }
  .poster {
    position: absolute; left: 225px; top: 69px;
    width: 750px; height: 1062px;
    background: linear-gradient(180deg, var(--navy) 0%, var(--mid-blue) 50%, var(--sky) 100%);
    box-shadow: 0 4px 14px rgba(0,0,0,.35);
    overflow: hidden;
  }
  .brand {
    position: absolute; left: 155px; top: 72px; width: 200px;
    display: flex; flex-direction: column; align-items: center;
    color: var(--white);
    font-family: "Nunito", sans-serif; font-weight: 800;
  }
  .brand-mark {
    width: 150px; height: 150px; border-radius: 50%;
    background: var(--gold); border: 5px solid var(--white);
  }
  .brand-name { margin-top: 18px; font-size: 46px; letter-spacing: 2px; line-height: 1; }
  .brand-sub { margin-top: 8px; font-size: 13px; letter-spacing: 3px; line-height: 1; }
  .links { position: absolute; left: 0; top: 0; }
  .values-list { list-style: none; }
  .value {
    position: absolute; left: 60px; width: 406px; height: 88px;
    border-radius: 44px; border: 4px solid var(--white);
    box-shadow: 4px 6px 8px rgba(0,0,0,.35);
    display: flex; align-items: center;
    color: var(--white);
    font-family: "Nunito", sans-serif; font-weight: 800; font-size: 29px;
  }
  .value-icon {
    width: 76px; height: 76px; margin-left: 2px; margin-right: 30px;
    border-radius: 50%; border: 3px solid var(--white);
    background: rgba(255,255,255,.14);
    display: flex; align-items: center; justify-content: center;
  }
  .value-icon svg { width: 42px; height: 42px; fill: none; stroke: var(--white); stroke-width: 2; stroke-linecap: round; stroke-linejoin: round; }
  .value--respect { top: 352px; background: var(--respect); }
  .value--responsibility { top: 487px; background: var(--responsibility); }
  .value--leadership { top: 621px; background: var(--leadership); }
  .value--pride { top: 756px; background: var(--pride); }
  .value--community { top: 890px; background: var(--community); }
  .headline {
    position: absolute; left: 570px; top: 62px; width: 160px;
    display: flex; flex-direction: column; align-items: center;
    color: var(--white);
    font-family: "Archivo", sans-serif; font-weight: 700; font-stretch: 125%;
    font-size: 108px; line-height: 80px;
  }
  .headline-word { display: flex; flex-direction: column; align-items: center; }
  .headline-word + .headline-word { margin-top: 104px; }
</style>
</head>
<body>
<main class="poster">
  <header class="brand">
    <div class="brand-mark"></div>
    <div class="brand-name">TAVI</div>
    <div class="brand-sub">ACADEMY</div>
  </header>

  <svg class="links" width="750" height="1062" aria-hidden="true">
    <g fill="none" stroke="#ffffff" stroke-width="3" stroke-dasharray="12 10">
      <ellipse cx="252" cy="463" rx="84" ry="72"/>
      <ellipse cx="252" cy="598" rx="84" ry="72"/>
      <ellipse cx="252" cy="732" rx="84" ry="72"/>
      <ellipse cx="252" cy="867" rx="84" ry="72"/>
    </g>
  </svg>

  <ul class="values-list">
    <li class="value value--respect">
      <span class="value-icon"><svg viewBox="0 0 40 40"><path d="M20 33 L7 20 A7 7 0 0 1 20 11 A7 7 0 0 1 33 20 Z"/><path d="M12 22 L18 17 L24 22 M16 25 L22 20"/></svg></span>
      RESPECT
    </li>
    <li class="value value--responsibility">
      <span class="value-icon"><svg viewBox="0 0 40 40"><circle cx="13" cy="10" r="3"/><circle cx="20" cy="8" r="3"/><circle cx="27" cy="10" r="3"/><path d="M9 19 a4 4 0 0 1 8 0 M16 17 a4 4 0 0 1 8 0 M23 19 a4 4 0 0 1 8 0"/><path d="M4 26 L12 24 Q20 27 28 25 L36 22 M4 32 L14 31 Q24 33 36 27"/></svg></span>
      RESPONSIBILITY
    </li>
    <li class="value value--leadership">
      <span class="value-icon"><svg viewBox="0 0 40 40"><path d="M4 34 H12 V27 H20 V20 H28 V13 H36"/><path d="M30 13 V3 L37 6 L30 9"/><circle cx="9" cy="22" r="2.5"/><circle cx="17" cy="15" r="2.5"/><circle cx="25" cy="8" r="2.5"/></svg></span>
      LEADERSHIP
    </li>
    <li class="value value--pride">
      <span class="value-icon"><svg viewBox="0 0 40 40"><path d="M12 34 L7 22 Q6 18 10 18 L14 22 V8 Q14 5 17 5 Q20 5 20 8 V20"/><path d="M20 14 Q23 12 26 14 L31 24 Q33 31 26 34 H18"/><path d="M30 6 L33 3 M34 11 L38 10 M25 5 L25 1"/></svg></span>
      PRIDE
    </li>
    <li class="value value--community">
      <span class="value-icon"><svg viewBox="0 0 40 40" style="fill:#ffffff;stroke:none"><circle cx="20" cy="12" r="5"/><circle cx="9" cy="15" r="4"/><circle cx="31" cy="15" r="4"/><path d="M11 32 Q11 19 20 19 Q29 19 29 32 Z"/><path d="M2 31 Q2 21 9 21 Q12 21 13 23 Q10 26 10 31 Z"/><path d="M38 31 Q38 21 31 21 Q28 21 27 23 Q30 26 30 31 Z"/></svg></span>
      COMMUNITY
    </li>
  </ul>

  <h1 class="headline">
    <span class="headline-word"><span>C</span><span>O</span><span>R</span><span>E</span></span>
    <span class="headline-word"><span>V</span><span>A</span><span>L</span><span>U</span><span>E</span><span>S</span></span>
  </h1>
</main>
</body>
</html>
```